EXPEDITE PROJECT: Brochure and Thank you card
Tri-Fold Brochure and Thank you card
A Tri-fold brochure and thank you card needed for my real estate management company.
Real Estate
target audience is mid size landlords in the Brooklyn NY area.
the size can be 8" X 11" 1/2 or 8" X 14". I will confirm this later on.
I have also attached the logo along with the content that is to be used on the brochure. Please see the attachment for that.
the colors scheme will probably be consistent with the logo Gray, black and white however i would like to see some more color options also please.
logo
i just uploaded a photo i like i was wondering if i can use it i found it on the web and brooklyn is my focus. never the less i want some imagery that says "BROOKLYN"
HERE IS MY NEW LAYOUT PLEASE USE THIS FOR DESIGNS
i think we can use this and play with it as we please
this picture is a must!!!! it is the brooklyn court house
we need a court picture maybe this can work
finalized version of text
almost finalized text

```html
<!DOCTYPE html>
<html lang="en">
<head>
<meta charset="utf-8">
<title>Hearth Key Partners — Brochure and Thank You Card</title>
<link rel="stylesheet" href="https://fonts.googleapis.com/css2?family=Cinzel:wght@400;700&family=Oswald:wght@400;500&family=Open+Sans:ital,wght@0,400;0,600;0,700;1,400&display=swap">
<style>
:root{
  --bg:#e6e6e4;
  --paper:#ffffff;
  --ink:#2b2b2b;
  --gray-dark:#4a4a4a;
  --gray-mid:#8a8a8a;
  --gray-light:#d4d4d4;
  --photo-brick-a:#6e5443;
  --photo-brick-b:#b8a58c;
  --photo-court-a:#3b3a36;
  --photo-court-b:#c9c2b3;
  --map-a:#1c1c1c;
  --map-b:#7b7b7b;
}
*{box-sizing:border-box;margin:0;padding:0}
html,body{width:1200px;height:813px;overflow:hidden;background:var(--bg)}
body{position:relative;font-family:"Open Sans",sans-serif;color:var(--ink)}
.sheet{position:absolute;background:var(--paper);display:flex;box-shadow:0 1px 4px rgba(0,0,0,.18)}
.sheet-outside{left:24px;top:22px;width:738px;height:378px}
.sheet-inside{left:24px;top:416px;width:738px;height:378px}
.panel{position:relative;width:246px;height:100%;overflow:hidden;border-right:1px dashed var(--gray-light)}
.panel:last-child{border-right:none}
.swoosh{position:absolute;left:0;top:0;width:100%;height:70px}
.brand{display:flex;flex-direction:column;align-items:center;gap:4px}
.brand-mark{width:14px;height:14px;background:var(--gray-dark)}
.brand-name{font-family:"Cinzel",serif;font-weight:700;color:var(--gray-dark);letter-spacing:.04em;text-align:center;line-height:1.15}
.photo{display:block}
/* outside panel 1 */
.headline{position:absolute;left:18px;top:74px;width:210px;font-family:"Oswald",sans-serif;font-weight:500;color:var(--gray-dark);text-transform:uppercase;font-size:25px;line-height:1.12}
.headline .big{font-size:38px;display:block}
.panel-intro .photo{position:absolute;left:18px;top:210px;width:210px;height:122px}
.web{position:absolute;bottom:12px;left:0;width:100%;text-align:center;font-size:8px;color:var(--gray-mid)}
/* contact panel */
.panel-contact .brand{position:absolute;top:90px;left:0;width:100%}
.panel-contact .brand-name{font-size:15px}
.contact{position:absolute;top:170px;left:0;width:100%;text-align:center;font-size:9px;line-height:1.55;color:var(--gray-dark)}
.contact h3{font-family:"Oswald",sans-serif;font-weight:500;font-size:14px;margin-bottom:4px;color:var(--ink)}
.contact .gap{height:8px}
/* cover */
.panel-cover .brand{position:absolute;top:72px;left:0;width:100%}
.panel-cover .brand-name{font-size:15px}
.tagline{position:absolute;top:138px;left:20px;width:206px;text-align:center;font-family:"Cinzel",serif;font-size:12px;line-height:1.4;color:var(--gray-dark)}
.panel-cover .photo{position:absolute;left:20px;top:196px;width:206px;height:128px}
.values{position:absolute;top:336px;left:0;width:100%;text-align:center;font-family:"Cinzel",serif;font-size:9px;color:var(--gray-mid);letter-spacing:.05em}
/* inside */
.panel-inside{padding:18px 14px 14px}
.lead{font-size:7.2px;line-height:1.5;color:var(--gray-dark);margin-bottom:8px}
.points{list-style:none;display:flex;flex-direction:column;gap:6px}
.points li{display:flex;gap:6px;align-items:flex-start;font-size:7px;line-height:1.4;color:var(--gray-dark)}
.tick{flex:0 0 11px;height:11px}
.section-title{font-family:"Oswald",sans-serif;font-weight:400;font-size:11px;color:var(--ink);margin:6px 0 4px;line-height:1.2}
.services{list-style:none;margin-bottom:6px}
.services li{font-size:7px;line-height:1.6;color:var(--gray-dark);padding-left:8px;position:relative}
.services li::before{content:"";position:absolute;left:0;top:4px;width:4px;height:4px;background:var(--gray-mid)}
.panel-services .web{font-size:7px}
.quotes{display:flex;flex-direction:column;gap:8px}
.quote{font-size:7px;line-height:1.45;color:var(--gray-dark);font-style:italic}
.quote cite{display:block;font-style:normal;font-weight:700;margin-top:1px}
/* thank you card */
.card{position:absolute;left:784px;top:22px;width:392px;height:258px;background:var(--paper);box-shadow:0 1px 4px rgba(0,0,0,.18);overflow:hidden}
.card .swoosh{height:60px}
.card .brand{position:absolute;left:20px;top:58px;width:150px}
.card .brand-name{font-size:13px}
.thanks{position:absolute;left:24px;top:124px;font-family:"Oswald",sans-serif;font-size:30px;color:var(--gray-dark);letter-spacing:.05em}
.card .gavel{position:absolute;left:24px;top:172px;width:150px;height:70px}
.card .map{position:absolute;right:18px;top:40px;width:180px;height:170px}
.card .borough{position:absolute;right:40px;top:216px;font-family:"Oswald",sans-serif;font-size:22px;font-weight:500;color:var(--ink);letter-spacing:.04em}
/* envelope */
.envelope{position:absolute;left:784px;top:300px;width:392px;height:250px;background:var(--paper);box-shadow:0 1px 4px rgba(0,0,0,.18);overflow:hidden}
.envelope .flap{position:absolute;left:0;top:0;width:100%;height:120px}
.envelope .brand{position:absolute;left:0;top:122px;width:100%}
.envelope .brand-name{font-size:14px}
.envelope .return{position:absolute;left:20px;bottom:18px;font-size:7px;line-height:1.5;color:var(--gray-mid)}
</style>
</head>
<body>

<!-- Brochure outside -->
<section class="sheet sheet-outside">
  <article class="panel panel-intro">
    <svg class="swoosh" viewBox="0 0 246 70" preserveAspectRatio="none"><path d="M0 0H246V26C170 54 80 30 0 60Z" fill="var(--gray-dark)"/><path d="M0 60C80 30 170 54 246 26V34C170 62 80 38 0 68Z" fill="var(--gray-light)"/></svg>
    <h1 class="headline">Servicing landlords for over <span class="big">10 years</span></h1>
    <svg class="photo" role="img" aria-label="Photo of a Brooklyn brownstone apartment building" viewBox="0 0 210 122" preserveAspectRatio="none"><defs><linearGradient id="brick" x1="0" y1="0" x2="1" y2="1"><stop offset="0" stop-color="var(--photo-brick-b)"/><stop offset="1" stop-color="var(--photo-brick-a)"/></linearGradient></defs><rect width="210" height="122" fill="url(#brick)"/></svg>
    <p class="web">www.hearthkeypartners.com</p>
  </article>

  <article class="panel panel-contact">
    <svg class="swoosh" viewBox="0 0 246 70" preserveAspectRatio="none"><path d="M0 0H246V50C170 24 80 52 0 28Z" fill="var(--gray-dark)"/><path d="M0 28C80 52 170 24 246 50V58C170 32 80 60 0 36Z" fill="var(--gray-light)"/></svg>
    <div class="brand"><span class="brand-mark"></span><span class="brand-name">Hearth Key Partners</span></div>
    <div class="contact">
      <h3>Contact Us</h3>
      <p>Hearth Key Partners</p>
      <p>420 Ashford Ave</p>
      <p>Brooklyn, NY 11201</p>
      <div class="gap"></div>
      <p>Office: 718-555-0142</p>
      <p>Fax: 718-555-0143</p>
      <p>Mobile: 917-555-0188</p>
      <p>Email: info@hearthkeypartners.com</p>
      <div class="gap"></div>
      <p>www.hearthkeypartners.com</p>
    </div>
  </article>

  <article class="panel panel-cover">
    <svg class="swoosh" viewBox="0 0 246 70" preserveAspectRatio="none"><path d="M0 0H246V22C160 50 70 20 0 44Z" fill="var(--gray-dark)"/></svg>
    <div class="brand"><span class="brand-mark"></span><span class="brand-name">Hearth Key Partners</span></div>
    <p class="tagline">A Full Service Realty Solution to Brooklyn Housing Court</p>
    <svg class="photo" role="img" aria-label="Photo of a judge's gavel and scales of justice" viewBox="0 0 206 128" preserveAspectRatio="none"><defs><linearGradient id="court" x1="0" y1="0" x2="1" y2="1"><stop offset="0" stop-color="var(--photo-court-b)"/><stop offset="1" stop-color="var(--photo-court-a)"/></linearGradient></defs><rect width="206" height="128" fill="url(#court)"/></svg>
    <p class="values">Reliable • Professional • Affordable</p>
  </article>
</section>

<!-- Brochure inside -->
<section class="sheet sheet-inside">
  <article class="panel panel-inside">
    <p class="lead">Hearth Key Partners has been serving Brooklyn property owners for more than ten years. We handle tenant matters, court filings and daily management so owners keep their time and their income.</p>
    <ul class="points">
      <li><svg class="tick" viewBox="0 0 11 11"><circle cx="5.5" cy="5.5" r="5.5" fill="var(--gray-dark)"/><path d="M3 5.6l1.8 1.8L8 4" stroke="#fff" stroke-width="1.3" fill="none"/></svg>We collect rent on time and keep a clear record of every payment.</li>
      <li><svg class="tick" viewBox="0 0 11 11"><circle cx="5.5" cy="5.5" r="5.5" fill="var(--gray-dark)"/><path d="M3 5.6l1.8 1.8L8 4" stroke="#fff" stroke-width="1.3" fill="none"/></svg>We screen every applicant before a lease is ever signed.</li>
      <li><svg class="tick" viewBox="0 0 11 11"><circle cx="5.5" cy="5.5" r="5.5" fill="var(--gray-dark)"/><path d="M3 5.6l1.8 1.8L8 4" stroke="#fff" stroke-width="1.3" fill="none"/></svg>Our attorney appears for you in housing court.</li>
      <li><svg class="tick" viewBox="0 0 11 11"><circle cx="5.5" cy="5.5" r="5.5" fill="var(--gray-dark)"/><path d="M3 5.6l1.8 1.8L8 4" stroke="#fff" stroke-width="1.3" fill="none"/></svg>We answer tenant calls so you do not have to.</li>
      <li><svg class="tick" viewBox="0 0 11 11"><circle cx="5.5" cy="5.5" r="5.5" fill="var(--gray-dark)"/><path d="M3 5.6l1.8 1.8L8 4" stroke="#fff" stroke-width="1.3" fill="none"/></svg>Repairs are scheduled with trusted local contractors.</li>
      <li><svg class="tick" viewBox="0 0 11 11"><circle cx="5.5" cy="5.5" r="5.5" fill="var(--gray-dark)"/><path d="M3 5.6l1.8 1.8L8 4" stroke="#fff" stroke-width="1.3" fill="none"/></svg>We track leases, renewals and every filing deadline.</li>
      <li><svg class="tick" viewBox="0 0 11 11"><circle cx="5.5" cy="5.5" r="5.5" fill="var(--gray-dark)"/><path d="M3 5.6l1.8 1.8L8 4" stroke="#fff" stroke-width="1.3" fill="none"/></svg>Monthly reports show exactly where your building stands.</li>
      <li><svg class="tick" viewBox="0 0 11 11"><circle cx="5.5" cy="5.5" r="5.5" fill="var(--gray-dark)"/><path d="M3 5.6l1.8 1.8L8 4" stroke="#fff" stroke-width="1.3" fill="none"/></svg>Fees are fair, flat and agreed in writing.</li>
      <li><svg class="tick" viewBox="0 0 11 11"><circle cx="5.5" cy="5.5" r="5.5" fill="var(--gray-dark)"/><path d="M3 5.6l1.8 1.8L8 4" stroke="#fff" stroke-width="1.3" fill="none"/></svg>One call reaches a team that knows Brooklyn.</li>
    </ul>
  </article>

  <article class="panel panel-inside panel-services">
    <h2 class="section-title">Our Services while leasing the apartment</h2>
    <ul class="services">
      <li>Screening all tenants for credit and history</li>
      <li>Preparing leases and renewals</li>
      <li>Showing the apartment</li>
      <li>Collecting deposits and first rent</li>
      <li>Move-in inspection report</li>
      <li>Key and lock handover</li>
    </ul>
    <h2 class="section-title">Our Services while using our attorney</h2>
    <ul class="services">
      <li>Court representation</li>
      <li>Nonpayment proceedings</li>
      <li>Holdover cases</li>
      <li>Stipulation review</li>
      <li>Lease violations</li>
      <li>Case tracking</li>
    </ul>
    <h2 class="section-title">Other services</h2>
    <ul class="services">
      <li>Rent collection</li>
      <li>Repair scheduling</li>
      <li>Insurance claims</li>
      <li>Landlord tenant advice</li>
    </ul>
    <p class="web">www.hearthkeypartners.com &nbsp;·&nbsp; 718-555-0142</p>
  </article>

  <article class="panel panel-inside">
    <h2 class="section-title">Testimonials</h2>
    <div class="quotes">
      <p class="quote">“They took over two difficult buildings and within months every unit was paying on time. I finally sleep at night.”<cite>Dana Whitfield, Owner</cite></p>
      <p class="quote">“Their attorney knew the court and the clerks. My case closed faster than I ever expected.”<cite>Marcus Oyelaran, Landlord</cite></p>
      <p class="quote">“Clear reports every month and a real person who answers the phone. That is rare in this business.”<cite>Irene Kowal, Property Owner</cite></p>
      <p class="quote">“I have worked with many managers. This team is honest, quick and always one step ahead of problems.”<cite>Sol Brenner, Investor</cite></p>
      <p class="quote">“Fair prices, steady tenants and no surprises. I recommend them to every owner I know.”<cite>Ruth Alvarado, Landlord</cite></p>
    </div>
  </article>
</section>

<!-- Thank you card -->
<section class="card">
  <svg class="swoosh" viewBox="0 0 392 60" preserveAspectRatio="none"><path d="M0 0H392V20C260 48 120 14 0 40Z" fill="var(--gray-dark)"/></svg>
  <div class="brand"><span class="brand-mark"></span><span class="brand-name">Hearth Key Partners</span></div>
  <p class="thanks">THANK YOU</p>
  <svg class="gavel" role="img" aria-label="Photo of a gavel resting on a law book" viewBox="0 0 150 70" preserveAspectRatio="none"><defs><linearGradient id="gavel" x1="0" y1="0" x2="1" y2="1"><stop offset="0" stop-color="var(--photo-court-b)"/><stop offset="1" stop-color="var(--photo-court-a)"/></linearGradient></defs><rect width="150" height="70" fill="url(#gavel)"/></svg>
  <svg class="map" role="img" aria-label="Word cloud illustration in the shape of a Brooklyn map" viewBox="0 0 180 170" preserveAspectRatio="none"><defs><radialGradient id="map" cx=".5" cy=".5" r=".6"><stop offset="0" stop-color="var(--map-b)"/><stop offset="1" stop-color="var(--map-a)"/></radialGradient></defs><rect width="180" height="170" fill="url(#map)"/></svg>
  <p class="borough">BROOKLYN</p>
</section>

<!-- Envelope -->
<section class="envelope">
  <svg class="flap" viewBox="0 0 392 120" preserveAspectRatio="none"><path d="M0 0H392L196 110Z" fill="var(--gray-dark)"/><path d="M0 0L196 110L392 0V6L196 118L0 6Z" fill="var(--gray-light)"/></svg>
  <div class="brand"><span class="brand-mark"></span><span class="brand-name">Hearth Key Partners</span></div>
  <p class="return">Hearth Key Partners<br>420 Ashford Ave<br>Brooklyn, NY 11201</p>
</section>

</body>
</html>
```